Update the A4 Specials Page for Restaurant/Cafe

Provide a MINIMALIST attractive Specials page we can print weekly for our food and drink specials to give to our guests. Final design is to be provided in WORD Document so it can be easily edited by Manager. Should be black text and MINIMALIST to minimise ink usage as we print hundreds a week. We have UPLOADED the existing page as a template for you to update. Maybe logo can stay, see what you think. Or delete it and do something else. Keep it simple. Choose a good FONT. Could be a little playful with a cocktail ICON or something. Our existing menus can be seen at www.tallpinebistro.com.au and they are using font Alegreya. Please note we are unable to provide any feedback to designers, however we really do appreciate your time if you are submitting a design. Thank you for your participation.

```html
<!DOCTYPE html>
<html lang="en">
<head>
<meta charset="utf-8">
<title>Tall Pine Bistro – Weekly Specials</title>
<link href="https://fonts.googleapis.com/css2?family=Alegreya:wght@400;700;900&display=swap" rel="stylesheet">
<style>
  :root {
    --ink: #151515;
    --leaf-tint: #f1f3f4;
    --paper: #ffffff;
    --backdrop: #eceeee;
  }
  * { margin: 0; padding: 0; box-sizing: border-box; }
  html, body { width: 1200px; height: 544px; overflow: hidden; }
  body {
    background: var(--backdrop);
    font-family: "Alegreya", Georgia, serif;
    color: var(--ink);
    position: relative;
  }
  .page {
    position: absolute;
    left: 408px; top: 0;
    width: 384px; height: 544px;
    background: var(--paper);
    overflow: hidden;
  }
  .leaf-area {
    position: absolute;
    background: var(--leaf-tint);
  }
  .leaf-area--top {
    right: 0; top: 0; width: 184px; height: 150px;
    background: linear-gradient(200deg, var(--leaf-tint) 0%, var(--leaf-tint) 45%, var(--paper) 100%);
  }
  .leaf-area--bottom {
    left: 0; bottom: 0; width: 180px; height: 160px;
    background: linear-gradient(20deg, var(--leaf-tint) 0%, var(--leaf-tint) 45%, var(--paper) 100%);
  }

  .brand {
    position: absolute; left: 40px; top: 26px;
    display: flex; align-items: center; gap: 7px;
  }
  .brand__mark { width: 16px; height: 16px; background: var(--ink); }
  .brand__name {
    font-weight: 900; font-size: 17px; letter-spacing: 0.4px;
    text-transform: uppercase; color: var(--ink); line-height: 1;
  }
  .title {
    position: absolute; left: 15px; top: 67px;
    font-size: 23px; font-weight: 400; line-height: 1.1; color: var(--ink);
  }
  .rule {
    position: absolute; left: 90px; top: 108px;
    width: 1px; height: 360px; background: var(--ink);
  }
  .item { position: absolute; left: 0; width: 384px; }
  .item__icon { position: absolute; left: 97px; width: 14px; height: 12px; }
  .item__name {
    position: absolute; left: 141px;
    font-weight: 900; font-size: 9.5px; line-height: 12px;
    text-transform: uppercase; letter-spacing: 0.1px;
  }
  .item__underline {
    position: absolute; left: 103px; width: 106px; height: 1px; background: var(--ink);
  }
  .item__heading {
    position: absolute; left: 116px;
    font-size: 15px; font-weight: 400;
    border-bottom: 1px solid var(--ink); line-height: 1.1;
  }
  .item__desc {
    position: absolute; left: 141px;
    font-size: 8.6px; line-height: 13px;
  }
  .item__price {
    position: absolute; right: 38px;
    font-size: 12px; font-weight: 700; line-height: 1;
  }
  .item__price sup { font-size: 6px; font-weight: 400; vertical-align: 5px; }
</style>
</head>
<body>
  <main class="page">
    <div class="leaf-area leaf-area--top" role="img" aria-label="Faint scattered leaf pattern"></div>
    <div class="leaf-area leaf-area--bottom" role="img" aria-label="Faint scattered leaf pattern"></div>

    <header class="brand">
      <span class="brand__mark"></span>
      <span class="brand__name">Tall Pine Bistro</span>
    </header>
    <h1 class="title">Weekly Specials</h1>
    <div class="rule"></div>

    <section class="item" style="top:129px">
      <svg class="item__icon" style="top:0" viewBox="0 0 14 12"><path d="M7 1 V8 M3 5 Q4 9 7 9 M11 5 Q10 8 7 9" stroke="#151515" stroke-width="1.5" fill="none" stroke-linecap="round"/></svg>
      <h2 class="item__name" style="top:0">Chicken Filo</h2>
      <div class="item__underline" style="top:12px"></div>
      <p class="item__desc" style="top:14px">Creamy Chicken with Pinenuts, wrapped in Filo Pastry.<br>Served with Side Salad &amp; Zulu Sauce</p>
      <p class="item__price" style="top:41px"><sup>$</sup>24</p>
    </section>

    <section class="item" style="top:212px">
      <svg class="item__icon" style="top:0" viewBox="0 0 14 12"><path d="M7 1 V8 M3 5 Q4 9 7 9 M11 5 Q10 8 7 9" stroke="#151515" stroke-width="1.5" fill="none" stroke-linecap="round"/></svg>
      <h2 class="item__name" style="top:0">Minestrone Soup</h2>
      <div class="item__underline" style="top:12px"></div>
      <p class="item__desc" style="top:13px">Served with Garlic Bread</p>
      <p class="item__price" style="top:28px;right:46px"><sup>$</sup>8</p>
    </section>

    <section class="item" style="top:282px">
      <svg class="item__icon" style="top:6px" viewBox="0 0 14 12"><path d="M7 1 V8 M3 5 Q4 9 7 9 M11 5 Q10 8 7 9" stroke="#151515" stroke-width="1.5" fill="none" stroke-linecap="round"/></svg>
      <h2 class="item__heading" style="top:0">Cocktail Special</h2>
      <h3 class="item__name" style="top:22px">Passionista</h3>
      <p class="item__desc" style="top:35px">Vodka, Passionfruit Pulp, Mango Puree<br>Top up with Ginger &amp; Lemon Kombucha</p>
      <p class="item__price" style="top:63px"><sup>$</sup>17</p>
    </section>

    <section class="item" style="top:388px">
      <svg class="item__icon" style="top:6px" viewBox="0 0 14 12"><path d="M7 1 V8 M3 5 Q4 9 7 9 M11 5 Q10 8 7 9" stroke="#151515" stroke-width="1.5" fill="none" stroke-linecap="round"/></svg>
      <h2 class="item__heading" style="top:0">Craft Beer Special</h2>
      <h3 class="item__name" style="top:22px;line-height:13px">Crooked Heron<br>Fruit Parade</h3>
      <p class="item__desc" style="top:48px">Tropical Pale Ale 4.8% Alc.</p>
      <p class="item__price" style="top:63px"><sup>$</sup>10</p>
    </section>
  </main>
</body>
</html>
```